Kelvar Systems Website

Website design for our company: Kelvar Systems.
The website should look fresh and IT focused. Please have a look at http://www.kelvarsystems.net.au/ for our current design. We want something fresh and new, professional looking, in WordPress so we can easily make changes.

Industry/Entity Type

It Company

```html
<!DOCTYPE html>
<html lang="en">
<head>
<meta charset="utf-8">
<title>Kelvar Systems</title>
<link href="https://fonts.googleapis.com/css2?family=Signika:wght@400;600&family=Arimo:wght@400;700&display=swap" rel="stylesheet">
<style>
:root{
  --green:#0bb04f;
  --green-dark:#079244;
  --dark:#3a3a3a;
  --darker:#474747;
  --text:#7a7a7a;
  --heading:#5a5a5a;
  --light:#f2f2f2;
  --white:#ffffff;
}
*{margin:0;padding:0;box-sizing:border-box}
html,body{width:1030px;height:1200px;overflow:hidden}
body{position:relative;font-family:"Arimo",Arial,sans-serif;color:var(--text);font-size:8px;
  background:linear-gradient(90deg,#c4c4c4 0%,#e9e9e9 22%,#f1f1f1 50%,#e9e9e9 78%,#c4c4c4 100%)}
.abs{position:absolute}
.head-font{font-family:"Signika",sans-serif}
/* header */
.topbar{left:0;top:0;width:1030px;height:62px;background:var(--dark)}
.logo{left:230px;top:11px;width:82px;height:41px;background:var(--green);border:2px solid var(--white);border-radius:3px;display:flex;align-items:center;justify-content:center;gap:4px;color:var(--white);font:700 10px "Arimo",sans-serif}
.logo i{width:7px;height:7px;background:var(--white);display:block}
.ip-note{left:634px;top:11px;color:var(--green);font-size:7.5px}
.search{left:635px;top:26px;width:92px;height:24px;border:1px solid #666;background:#3e3e3e;color:#aaa;font-size:7px;padding:7px 6px}
.radio{top:33px;display:flex;align-items:center;gap:5px;color:#ccc;font-size:7px;font-weight:700}
.radio i{width:8px;height:8px;border-radius:50%;background:#777;display:block}
.green-band{left:0;top:62px}
.nav{top:76px;right:197px;display:flex;gap:14px;font:600 9px "Signika",sans-serif;color:var(--white);letter-spacing:.4px}
.nav span.active{border-bottom:3px solid var(--white);padding-bottom:6px}
/* slider */
.slider{left:229px;top:112px;width:604px;height:212px;background:var(--white);padding:5px}
.slider-inner{width:100%;height:100%;background:linear-gradient(90deg,#f7f7f7,#ececec);position:relative}
.slide-art{position:absolute;left:0;top:0;width:380px;height:100%;background:linear-gradient(100deg,#e6e6e6 0%,#2b2b2b 20%,#4a4a4a 45%,#d9d9d9 65%,#bfc3c8 85%,#eeeeee 100%)}
.slide-copy{position:absolute;right:90px;top:60px;text-align:right}
.slide-copy .s1{font:400 13px "Signika",sans-serif;color:var(--green)}
.slide-copy .s2{font:600 17px "Signika",sans-serif;color:var(--green);letter-spacing:.8px}
.slide-copy p{font-size:7.5px;color:#555;line-height:10px;margin-top:6px}
.btn{background:var(--green);color:var(--white);font:600 8.5px "Signika",sans-serif;display:flex;align-items:center;justify-content:center;letter-spacing:.4px}
.slide-btn{position:absolute;right:97px;top:127px;width:76px;height:25px}
.dots{left:512px;top:339px;display:flex;gap:3px}
.dots i{width:8px;height:8px;border-radius:50%;background:#666;border:1px solid #999;display:block}
.dots i.on{background:var(--green)}
.tagline{left:229px;top:368px;width:604px;height:29px;background:linear-gradient(90deg,#d0d0d0,#dedede 50%,#d0d0d0);display:flex;align-items:center;justify-content:center;font-size:7.5px;font-weight:700;color:#555}
/* features */
.feature{top:418px;width:176px}
.feature .pic{height:94px}
.feature h4{font:700 8.5px "Arimo",sans-serif;color:var(--green);margin-top:11px}
.feature p{font-size:7.5px;line-height:9.5px;margin-top:5px}
.rule{left:229px;width:604px;border-top:1px dashed #b5b5b5}
h2.sec{font:400 14px "Signika",sans-serif;color:var(--heading);letter-spacing:.6px}
h2.sec b{color:var(--green);font-weight:400}
.welcome{left:230px;top:598px;width:390px}
.welcome p{font-size:7.5px;line-height:9.5px;margin-top:10px}
.welcome h2+p{margin-top:17px}
.more{color:var(--green);font-size:7px;margin-top:12px;display:block}
.services{left:656px;top:598px}
.services ul{list-style:none;margin-top:14px}
.services li{display:flex;align-items:center;gap:9px;font-size:7.5px;height:15.6px}
/* news */
.news{left:230px;top:789px;width:175px}
.news-item{display:flex;gap:12px;height:51px;border-bottom:1px solid #cfcfcf;padding-top:12px}
.news-item:first-of-type{margin-top:14px}
.date{width:26px;text-align:center;font:400 13px "Signika",sans-serif;color:#999}
.date .d{background:var(--white);border:1px solid #ddd;height:20px}
.date .m{font-size:7px;color:#aaa;margin-top:2px}
.news-item h5{font:400 8px "Signika",sans-serif;color:#666}
.news-item p{font-size:6.5px;line-height:9px;margin-top:4px}
.remote{left:438px;top:789px}
.remote-box{margin-top:14px;width:175px;height:108px;background:var(--white);padding:14px 15px;box-shadow:0 10px 8px -8px rgba(0,0,0,.25)}
.remote-box .label{font-size:8px;color:#666}
.remote-box .field{margin-top:12px;height:24px;background:#e6e6e6}
.remote-box .btn{margin-top:9px;width:78px;height:21px;font-size:9px}
.testimonial{left:655px;top:789px;width:180px}
.quote{margin-top:20px;padding:0 10px 0 18px;font-size:7.5px;line-height:9.5px;position:relative;color:#666}
.quote .q{position:absolute;font:700 18px Georgia,serif;color:var(--green)}
.person{margin-top:18px;display:flex;gap:20px;align-items:center}
.person .pic{width:78px;height:52px;background:linear-gradient(120deg,#6b4a3a,#d8b39b 55%,#8b6b5b)}
.person .name{text-align:right;color:var(--green);font-size:9px}
.person .name small{display:block;color:#777;font-size:6.5px;margin-top:4px}
/* footer */
.footer{left:0;top:994px;width:1030px;height:176px;background:var(--dark)}
.footer h2.sec{color:#e5e5e5}
.fcol{top:1018px}
.contact-line{display:flex;gap:14px;font-size:7.5px;color:#bbb;line-height:12px;margin-top:6px}
.contact-line svg{flex:none;margin-top:2px}
.tweet{font-size:7px;color:#999;line-height:9px;margin-top:18px;width:180px}
.tweet b{color:var(--green);font-weight:400}
.tweet small{display:block;color:#ccc;font-size:5.5px;margin-top:2px}
.tweet+.tweet{border-top:1px solid #555;padding-top:12px;margin-top:12px}
.email{margin-top:18px;width:136px;height:26px;border:1px solid #666;display:flex;justify-content:space-between;align-items:center;padding:0 10px;font-size:6.5px;color:#999}
.email span{color:var(--green);font-size:12px}
.social{display:flex;gap:4px;margin-top:10px}
.social i{width:15px;height:15px;border-radius:50%;background:#bdbdbd;display:block}
.bottombar{left:0;top:1170px;width:1030px;height:30px;background:var(--darker);color:#ddd;font-size:6px}
.copyright{left:230px;top:12px}
.foot-nav{right:197px;top:12px;display:flex;gap:9px;font-weight:700}
</style>
</head>
<body>
<div class="abs topbar"></div>
<div class="abs logo"><i></i>Kelvar Systems</div>
<div class="abs ip-note">Your IP address is 203.0.113.24 which resolves to 203.0.113.24</div>
<div class="abs search">Search</div>
<div class="abs radio" style="left:734px"><i></i>Site</div>
<div class="abs radio" style="left:772px"><i></i>Web</div>

<svg class="abs green-band" width="1030" height="120" viewBox="0 0 1030 120" aria-hidden="true">
  <polygon points="0,0 1030,0 1030,114 830,88 230,88 0,58" fill="#0bb04f"/>
</svg>
<nav class="abs nav">
  <span class="active">HOME</span><span>CLIENTS</span><span>SERVICES</span><span>SUPPORTS</span><span>TESTIMONIALS</span><span>CONTACT US</span><span>ABOUT US</span>
</nav>

<section class="abs slider">
  <div class="slider-inner">
    <div class="slide-art" role="img" aria-label="Laptop showing the website beside large grey puzzle pieces"></div>
    <div class="slide-copy">
      <div class="s1">Simplify</div>
      <div class="s2">YOUR BUSINESS</div>
      <p>Create a refreshing customer experience<br>that's free of complexity and confusion</p>
    </div>
    <div class="btn slide-btn">READ MORE</div>
  </div>
</section>
<div class="abs dots"><i></i><i class="on"></i><i></i><i></i></div>
<div class="abs tagline">Kelvar Systems is an Adelaide based company with a single objective - to excel in the support and service of all computer and IT needs</div>

<div class="abs feature" style="left:230px">
  <div class="pic" role="img" aria-label="Globe clock resting on banknotes" style="background:linear-gradient(120deg,#e9e4d8,#b9b9b9 50%,#f4f4f4)"></div>
  <h4>Lorem Ipsum is simply dummy text</h4>
  <p>Lorem Ipsum is simply dummy text of the printing and typesetting industry</p>
</div>
<div class="abs feature" style="left:438px">
  <div class="pic" role="img" aria-label="Computer monitor and keyboard on a desk" style="background:linear-gradient(120deg,#2f3a4a,#6fa6d8 45%,#d8dde2 80%,#9aa2aa)"></div>
  <h4>Lorem Ipsum is simply dummy text</h4>
  <p>Lorem Ipsum is simply dummy text of the printing and typesetting industry</p>
</div>
<div class="abs feature" style="left:656px">
  <div class="pic" role="img" aria-label="Office computers and keyboards in soft blue light" style="background:linear-gradient(120deg,#4c5964,#9aa7b2 50%,#3a434b)"></div>
  <h4>Lorem Ipsum is simply dummy text</h4>
  <p>Lorem Ipsum is simply dummy text of the printing and typesetting industry</p>
</div>

<div class="abs rule" style="top:577px"></div>

<section class="abs welcome">
  <h2 class="sec">WELCOME TO <b>OUR COMPANY</b></h2>
  <p>Kelvar Systems is an Adelaide based company with a single objective - to excel in the support and service of all computer and IT needs.</p>
  <p style="margin-top:6px">We provide a high level of consulting services using the most experienced engineers at a reasonable and fair price. We believe in using a Business Value approach to every aspect of computer consulting to provide our clients with the most cost effective solutions.</p>
  <p>We strongly believe that we are in business with our clients. Each thing we do must be measured against our clients' business objectives. At the end of the day our client's success is our success.</p>
  <span class="more">Read More &rarr;</span>
</section>

<section class="abs services">
  <h2 class="sec">OUR <b>SERVICES</b></h2>
  <ul>
    <li><svg width="9" height="9" viewBox="0 0 9 9"><path d="M1 5l2.5 2.5L8 1" stroke="#888" stroke-width="1.6" fill="none"/></svg>On-site Service</li>
    <li><svg width="9" height="9" viewBox="0 0 9 9"><path d="M1 5l2.5 2.5L8 1" stroke="#888" stroke-width="1.6" fill="none"/></svg>Remote Desktop Support</li>
    <li><svg width="9" height="9" viewBox="0 0 9 9"><path d="M1 5l2.5 2.5L8 1" stroke="#888" stroke-width="1.6" fill="none"/></svg>Medical IT Service</li>
    <li><svg width="9" height="9" viewBox="0 0 9 9"><path d="M1 5l2.5 2.5L8 1" stroke="#888" stroke-width="1.6" fill="none"/></svg>Pharmacy IT Service</li>
    <li><svg width="9" height="9" viewBox="0 0 9 9"><path d="M1 5l2.5 2.5L8 1" stroke="#888" stroke-width="1.6" fill="none"/></svg>Disaster Recovery</li>
    <li><svg width="9" height="9" viewBox="0 0 9 9"><path d="M1 5l2.5 2.5L8 1" stroke="#888" stroke-width="1.6" fill="none"/></svg>Hardware/ Software supply</li>
    <li><svg width="9" height="9" viewBox="0 0 9 9"><path d="M1 5l2.5 2.5L8 1" stroke="#888" stroke-width="1.6" fill="none"/></svg>Consumables</li>
  </ul>
</section>

<div class="abs rule" style="top:768px"></div>

<section class="abs news">
  <h2 class="sec">LATEST <b>NEWS</b></h2>
  <div class="news-item"><div class="date"><div class="d">04</div><div class="m">MAY</div></div><div><h5>Latest News Heading Here</h5><p>Lorem Ipsum is simply dummy text of the printing and typesetting industry</p></div></div>
  <div class="news-item"><div class="date"><div class="d">06</div><div class="m">MAY</div></div><div><h5>Latest News Heading Here</h5><p>Lorem Ipsum is simply dummy text of the printing and typesetting industry</p></div></div>
  <div class="news-item" style="border:0"><div class="date"><div class="d">08</div><div class="m">MAY</div></div><div><h5>Latest News Heading Here</h5><p>Lorem Ipsum is simply dummy text of the printing and typesetting industry</p></div></div>
</section>

<section class="abs remote">
  <h2 class="sec">REMOTE <b>SUPPORT</b></h2>
  <div class="remote-box">
    <div class="label">Enter your 6-digit code</div>
    <div class="field"></div>
    <div class="btn">Connect Now</div>
  </div>
</section>

<section class="abs testimonial">
  <h2 class="sec">CLIENTS <b>TESTIMONIAL</b></h2>
  <div class="quote"><span class="q" style="left:0;top:-8px">&ldquo;</span>Lorem Ipsum is simply dummy text of the printing and typesetting industry. Lorem Ipsum has been the industry's standard dummy text ever since the 1500s<span class="q" style="right:0;bottom:-18px">&rdquo;</span></div>
  <div class="person">
    <div class="pic" role="img" aria-label="Portrait photo of the client"></div>
    <div class="name">Norvane Technology<small>Web Design &amp; Developer, IND</small></div>
  </div>
</section>

<footer class="abs footer"></footer>
<section class="abs fcol" style="left:230px">
  <h2 class="sec">CONTACT <b>US</b></h2>
  <div class="contact-line" style="margin-top:14px"><svg width="10" height="9" viewBox="0 0 10 9"><path d="M0 4l5-4 5 4v5H0z M0 4l5 3 5-3" stroke="#bbb" fill="none"/></svg><span>412 Harbour Lane<br>Westbrook Park<br>5020<br>Australia</span></div>
  <div class="contact-line"><svg width="10" height="9" viewBox="0 0 10 9"><path d="M2 0h2l1 2-1.5 1.2a6 6 0 003 3L8 5l2 1v2c-5 1-10-4-8-8z" fill="#bbb"/></svg><span>0855501234</span></div>
  <div class="contact-line" style="margin-top:3px"><svg width="10" height="9" viewBox="0 0 10 9"><rect x="1" y="0" width="8" height="9" fill="#bbb"/></svg><span>085550 4400</span></div>
  <div class="contact-line" style="margin-top:3px"><svg width="10" height="9" viewBox="0 0 10 9"><rect x="2.5" y="0" width="5" height="9" rx="1" fill="#bbb"/></svg><span>0855501234</span></div>
</section>
<section class="abs fcol" style="left:438px">
  <h2 class="sec">GET IN <b>TWEET</b></h2>
  <div class="tweet"><b>@companyname</b> Lorem Ipsum is simply dummy text of the printing and typesetting industry<small>5 min ago</small></div>
  <div class="tweet"><b>@companyname</b> Lorem Ipsum is simply dummy text of the printing and typesetting industry<small>5 min ago</small></div>
</section>
<section class="abs fcol" style="left:656px">
  <h2 class="sec">NEWSLETTER <b>SIGNUP</b></h2>
  <div class="email">Your Email<span>&rsaquo;</span></div>
  <h2 class="sec" style="margin-top:22px">FOLLOW <b>US</b></h2>
  <div class="social"><i></i><i></i><i></i><i></i><i></i><i></i></div>
</section>

<div class="abs bottombar">
  <div class="abs copyright">Copyright &copy; 2014 Kelvar Systems Pty Ltd. All Rights Reserved.</div>
  <div class="abs foot-nav"><span>HOME</span><span>CLIENTS</span><span>SERVICES</span><span>SUPPORTS</span><span>TESTIMONIALS</span><span>CONTACT US</span><span>ABOUT US</span></div>
</div>
</body>
</html>
```